International Rescue Training Company needs website redesign

Vantor 7 Global is a worldwide rescue training and accreditation company. We deliver water, rope, and medical training courses to emergency services, industry, government and outdoor adventure companies. We are currently looking to completely redesign our website. The main goals of this redesign are as follows:
1. Modernize the look of the website.
2. Make the website mobile compatible.
3. Focus on the international aspect of the business by making it less US focused than the current site. The new site will show us as an international brand. A separate (but similar) US site will be developed for the US market, similar in concept (but not design) to the one in place for our European office (www.vantor7europe.example).

The winning design should have:
1. Fully coded website
2. A modern, responsive design that would appeal to people in the emergency services, industrial and adventure recreation industries. Our courses are hands on, energetic, and fast paced and that should be conveyed in the design.
3. A navigation bar either at the top or side of the webpage (see attached document for page organization
4. 4 page designs: home page, template page, contact page, find a training provider page (interactive world map)

Still images and some video can be provided to aid in the design process.

Winning designer may be asked to consult on second US site.

Target Market(s)

Emergency Services (Fire, Police, Search and Rescue, Military)
Industrial Companies (Mines, Oil, Tower, etc)
Government (resource management, park rangers, road workers, etc)
Outdoor adventure companies and individuals (rafting, kayaking, highline, etc)

Industry/Entity Type

Training

Coding

Coded - Design and coding required

Number of Pages Required

4 page

Requirements
Must have
• 1. Fully coded
• 2. Mobile responsive design
• 3. Navigation bar
Nice to have
• -Dynamic images and videos
• -Interactive map or something similar so people can find a training provider in their region
Should not have
• Loud, bright, or pastel colors.

```html
<!DOCTYPE html>
<html lang="en">
<head>
<meta charset="utf-8">
<title>Vantor 7 Global – Rescue Training Programs &amp; Courses</title>
<link rel="stylesheet" href="https://fonts.googleapis.com/css2?family=Source+Sans+3:wght@400;600&family=Arimo:wght@400&display=swap">
<style>
:root{
  --navy:#0b3f74;
  --navy-deep:#062f5a;
  --title-blue:#0d4a87;
  --green-top:#6cbf3e;
  --green-bottom:#3f9a22;
  --page:#ffffff;
  --card-bg:#f2f2f2;
  --card-line:#c9c9c9;
  --text:#4a4a4a;
  --muted:#9a9a9a;
  --footer-text:#e6eef7;
  --bar:#000000;
}
*{box-sizing:border-box;margin:0;padding:0}
html,body{width:999px;height:1200px;overflow:hidden}
body{background:linear-gradient(#0b4a86,#083766);font-family:"Source Sans 3",sans-serif}
.stage{position:absolute;left:0;top:0;width:1066px;height:1280px;transform:scale(0.9375);transform-origin:0 0}
.abs{position:absolute}
.page-white{left:32px;top:33px;width:1000px;height:974px;background:var(--page)}
.logo-box{left:46px;top:45px;width:323px;height:85px;background:#e4e4e4;display:flex;align-items:center;justify-content:center;color:#777;font-size:30px}
.btn{display:flex;align-items:center;justify-content:center;color:#fff;font-size:15px;border-radius:8px}
.btn-green{background:linear-gradient(var(--green-top),var(--green-bottom))}
.btn-navy{background:var(--navy)}
.search-bar{left:697px;top:66px;width:314px;height:55px;background:var(--navy);border-radius:10px}
.field{background:#fff;color:var(--muted);font-style:italic;font-weight:600;font-size:17px;padding-left:14px;display:flex;align-items:center}
.search-go{left:963px;top:66px;width:48px;height:55px;border-radius:0 10px 10px 0}
.nav-band{left:32px;top:143px;width:1000px;height:28px;background:linear-gradient(var(--green-top),var(--green-bottom))}
.main-nav{left:650px;top:143px;height:28px;display:flex;align-items:center;color:#fff;font-size:12px}
.main-nav span{margin:0 21px 0 0}
.main-nav .sep{margin-right:25px}
.hero-photo{left:32px;top:180px;width:680px;height:433px;background:linear-gradient(90deg,#1d3f6e 0%,#5c93c7 35%,#89bde0 60%,#c6dbe8 85%,rgba(255,255,255,0) 100%)}
.hero-title{right:56px;top:214px;text-align:right;color:var(--title-blue);font-size:40px;line-height:48px}
.hero-rule{left:652px;top:325px;width:364px;height:1px;background:var(--green-bottom)}
.hero-copy{left:690px;top:339px;width:320px;text-align:right;color:var(--text);font-size:17.5px;line-height:21.5px}
.finder{left:427px;top:493px;width:605px;height:120px;background:var(--navy)}
.band-lower{left:32px;top:613px;width:1000px;height:28px;background:linear-gradient(var(--green-top),var(--green-bottom))}
.card{width:313px;height:290px;top:681px;background:var(--card-bg);border:1px solid var(--card-line)}
.card-head{position:absolute;left:11px;top:8px;width:290px;height:42px;background:linear-gradient(var(--green-top),var(--green-bottom));color:#fff;font-size:29px;display:flex;align-items:center;justify-content:center}
.card-rule{position:absolute;left:13px;width:287px;height:1px;background:#dadada}
.card-photo{position:absolute;left:11px;top:83px;width:138px;height:129px}
.card-text{position:absolute;left:159px;top:79px;width:142px;font-family:"Arimo",sans-serif;font-size:13px;line-height:16.8px;color:var(--text)}
.view-btn{position:absolute;left:95px;top:244px;width:125px;height:26px;border-radius:13px;background:var(--navy);color:#fff;font-family:"Arimo",sans-serif;font-size:11.5px;display:flex;align-items:center;justify-content:center}
.footer-col{top:1036px;width:170px}
.footer-col h3{font-weight:400;font-size:20px;color:var(--footer-text);padding-bottom:8px;border-bottom:1px solid #4f7fb0;margin-bottom:13px}
.footer-col a{display:block;color:#fff;text-decoration:none;font-family:"Arimo",sans-serif;font-size:14.5px;line-height:26.5px}
.bottom-bar{left:32px;top:1183px;width:1000px;height:56px;background:var(--bar)}
.bottom-nav{left:347px;top:1183px;height:56px;display:flex;align-items:center;color:#bbb;font-family:"Arimo",sans-serif;font-size:12px}
.bottom-nav span{margin-right:32px}
.social{top:1197px;width:27px;height:27px;border-radius:50%;background:var(--green-top)}
</style>
</head>
<body>
<div class="stage">
  <div class="abs page-white"></div>

  <header>
    <div class="abs logo-box">YOUR LOGO</div>
    <a class="abs btn btn-green" style="left:513px;top:75px;width:79px;height:36px">Login</a>
    <a class="abs btn btn-navy" style="left:601px;top:75px;width:79px;height:36px">Sign up</a>
    <div class="abs search-bar"></div>
    <div class="abs field" style="left:712px;top:78px;width:237px;height:30px">search</div>
    <div class="abs btn btn-green search-go">
      <svg width="28" height="28" viewBox="0 0 28 28" aria-hidden="true"><circle cx="16" cy="12" r="8" fill="none" stroke="#fff" stroke-width="3"/><line x1="10" y1="18" x2="4" y2="24" stroke="#fff" stroke-width="4" stroke-linecap="round"/></svg>
    </div>
    <div class="abs nav-band"></div>
    <nav class="abs main-nav">
      <span>HOME</span><span class="sep">|</span><span>ABOUT</span><span class="sep">|</span><span>SERVICES</span><span class="sep">|</span><span>CONTACT</span>
    </nav>
  </header>

  <section class="hero">
    <div class="abs hero-photo" role="img" aria-label="Photo of a team of smiling medical rescue instructors in scrubs with stethoscopes"></div>
    <h1 class="abs hero-title" style="font-weight:400">Rescue Training<br>Programs &amp; Courses</h1>
    <div class="abs hero-rule"></div>
    <p class="abs hero-copy">Lorem ipsum dolor sit amet consectetur adipiscing elit lorem ipsum dolor sit amet consectetur adipiscing elit.</p>
    <a class="abs btn btn-green" style="left:783px;top:428px;width:108px;height:36px">Learn More</a>
    <a class="abs btn btn-navy" style="left:901px;top:428px;width:109px;height:36px;border:1px solid #1c5590">Rate Now</a>

    <div class="abs finder"></div>
    <div class="abs field" style="left:452px;top:517px;width:237px;height:30px">City, State</div>
    <div class="abs field" style="left:702px;top:517px;width:237px;height:30px">Institution</div>
    <div class="abs field" style="left:452px;top:563px;width:237px;height:30px">Type of program</div>
    <div class="abs field" style="left:702px;top:563px;width:237px;height:30px">Key Words</div>
    <div class="abs btn btn-green" style="left:945px;top:559px;width:61px;height:36px;border-radius:6px">
      <svg width="26" height="26" viewBox="0 0 28 28" aria-hidden="true"><circle cx="16" cy="12" r="8" fill="none" stroke="#fff" stroke-width="3"/><line x1="10" y1="18" x2="4" y2="24" stroke="#fff" stroke-width="4" stroke-linecap="round"/></svg>
    </div>
    <div class="abs band-lower"></div>
  </section>

  <section class="cards">
    <article class="abs card" style="left:49px">
      <div class="card-head">Training Programs</div>
      <div class="card-rule" style="top:65px"></div>
      <div class="card-photo" role="img" aria-label="Photo of a smiling doctor with a stethoscope in a clinic" style="background:linear-gradient(135deg,#d9c7b4,#eef2f5 60%,#9fb9d2)"></div>
      <p class="card-text">lorem ipsum dolor sit amet consectetur und adipiscing elit sit amet lorem ipsum dolor sit amet consectetur und elit sit amet ipsum sit elit. ipsum lorem</p>
      <div class="card-rule" style="top:228px"></div>
      <a class="view-btn">VIEW DETAILS</a>
    </article>
    <article class="abs card" style="left:374px">
      <div class="card-head">Institutions</div>
      <div class="card-rule" style="top:65px"></div>
      <div class="card-photo" role="img" aria-label="Photo of a brick training center building under a cloudy sky" style="background:linear-gradient(#8fa9c4 0%,#c9d3dc 35%,#a0674a 55%,#8c6a55 80%,#7b7b78 100%)"></div>
      <p class="card-text">lorem ipsum dolor sit amet consectetur und adipiscing elit sit amet lorem ipsum dolor sit amet consectetur und adipiscing elit sit amet sit consectetur elit.</p>
      <div class="card-rule" style="top:228px"></div>
      <a class="view-btn">VIEW DETAILS</a>
    </article>
    <article class="abs card" style="left:698px;width:314px">
      <div class="card-head">Statistics</div>
      <div class="card-rule" style="top:65px"></div>
      <div class="card-photo" role="img" aria-label="Photo of a modern glass hospital entrance with landscaped garden" style="background:linear-gradient(#b5c6d6 0%,#dfe5ea 30%,#6d8196 60%,#6f7a53 82%,#8a6b6b 100%)"></div>
      <p class="card-text">lorem ipsum dolor sit amet consectetur und adipiscing elit sit amet lorem ipsum dolor und adipiscing elit sit amet lorem adipiscing sit consectetur.</p>
      <div class="card-rule" style="top:228px"></div>
      <a class="view-btn">VIEW DETAILS</a>
    </article>
  </section>

  <footer>
    <div class="abs footer-col" style="left:98px"><h3>About Us</h3><a>General Information</a><a>Our Mission</a></div>
    <div class="abs footer-col" style="left:338px"><h3>Customer Reviews</h3><a>Adipiscing Elit</a><a>Ipsum Lorem Sit Amet</a></div>
    <div class="abs footer-col" style="left:578px"><h3>Support Materials</h3><a>Lorem ipsum</a><a>Dolor Sit Amet Consectetur</a></div>
    <div class="abs footer-col" style="left:828px"><h3>Contact Us</h3><a>Facepage</a><a>Chirper</a><a>Email us</a></div>

    <div class="abs bottom-bar"></div>
    <nav class="abs bottom-nav">
      <span>HOME</span><span>|</span><span>ABOUT</span><span>|</span><span>REVIEWS</span><span>|</span><span>CONTACT</span>
    </nav>
    <span class="abs social" style="left:870px" aria-label="Facepage"></span>
    <span class="abs social" style="left:921px" aria-label="Chirper"></span>
    <span class="abs social" style="left:973px" aria-label="Pin board"></span>
  </footer>
</div>
</body>
</html>
```